Business Card design for a skin clinic

i would like a business card design for our skin clinic.
our logo colors are Blue and Grey and Bule /white.
we are searching for a minimalistic design yet very elegant,dynamic and professional which can reflect a professional medical skin care clinic( not a beauty salon).
THE DESGIN IS NOT FOR A PERSON IT WILL BE USED IN THE CLINIC FOR CLIENTS SO THERE SHOULD BE NO NAME OF A PERSON ONLY THE CLINIC NAME AND THE CONTACT INFO

Target Market(s)
young and old womens
Industry/Entity Type
Business
Contact Information for Business Card
we have 2 address and both should be on the card.
address A: Lindenhofkade 42B, 3017KP Rotterdam, Tel 010 438 21 95
address B: Zonnewijzerstraat 73, 1062HT Amsterdam Tel 020 519 8372
website www.velorahuid.nu, email info@velorahuid.nu
Look and feel

```html
<!DOCTYPE html>
<html lang="nl">
<head>
<meta charset="utf-8">
<title>Velora Huid – Visitekaartje</title>
<link href="https://fonts.googleapis.com/css2?family=Josefin+Sans:wght@400;600&family=Open+Sans:wght@400;600&display=swap" rel="stylesheet">
<style>
  :root {
    --canvas-bg: #ecebe8;
    --card-dark: #19202a;
    --card-light: #ffffff;
    --brand-blue: #2f86c9;
    --brand-grey: #4f5257;
    --text-grey: #454545;
    --tag-grey: #6d6f73;
    --rule-grey: #8a8a8a;
    --white: #ffffff;
  }
  * { box-sizing: border-box; margin: 0; padding: 0; }
  html, body {
    width: 1200px; height: 1000px; overflow: hidden;
    background: var(--canvas-bg);
  }
  .canvas { position: relative; width: 1200px; height: 1000px; }

  .card {
    position: absolute; left: 266px; width: 666px; height: 397px;
    box-shadow: 0 3px 10px rgba(0,0,0,0.18);
  }
  .card--front { top: 74px; background: var(--card-dark); }
  .card--back  { top: 533px; background: var(--card-light); }

  .brand-mark {
    position: absolute; background: var(--brand-blue);
  }
  .brand-name {
    position: absolute; left: 0; right: 0; text-align: center;
    font-family: "Josefin Sans", sans-serif; font-weight: 400;
    letter-spacing: 0.06em; white-space: nowrap;
  }
  .tagline {
    position: absolute; left: 0; right: 0; text-align: center;
    font-family: "Josefin Sans", sans-serif; font-weight: 400;
    letter-spacing: 0.12em; white-space: nowrap;
  }

  /* front */
  .card--front .brand-mark { left: 318px; top: 120px; width: 30px; height: 30px; }
  .card--front .brand-name { top: 222px; font-size: 46px; color: var(--white); }
  .card--front .tagline { top: 281px; font-size: 18px; color: #e8eaed; }

  /* back */
  .back-brand { position: absolute; left: 0; top: 0; width: 340px; height: 397px; }
  .card--back .brand-mark { left: 158px; top: 152px; width: 24px; height: 24px; }
  .card--back .brand-name { top: 212px; font-size: 34px; color: var(--brand-blue); }
  .card--back .tagline { top: 259px; font-size: 13px; color: var(--tag-grey); }

  .divider {
    position: absolute; left: 339px; top: 78px; width: 1px; height: 240px;
    background: var(--rule-grey);
  }

  .contact {
    position: absolute; left: 372px; top: 72px; width: 280px;
    font-family: "Open Sans", sans-serif; color: var(--text-grey);
    font-size: 16px; line-height: 20px;
  }
  .contact__title {
    font-weight: 600; font-size: 19px; line-height: 24px;
    color: var(--brand-grey); margin-bottom: 14px; letter-spacing: 0.01em;
  }
  .contact__title .accent { color: var(--brand-blue); }
  .contact__address { margin-bottom: 5px; }
  .contact__line { display: flex; align-items: center; gap: 7px; height: 21px; }
  .contact__line + .contact__address { margin-top: 10px; }
  .contact__line--email { margin-top: 12px; }
  .contact__line--web { margin-top: 5px; }
  .icon { width: 14px; height: 14px; flex: none; fill: var(--brand-blue); }
</style>
</head>
<body>
<div class="canvas">

  <section class="card card--front">
    <span class="brand-mark"></span>
    <div class="brand-name">VELORA HUID</div>
    <div class="tagline">next generation skin care</div>
  </section>

  <section class="card card--back">
    <div class="back-brand">
      <span class="brand-mark"></span>
      <div class="brand-name">VELORA HUID</div>
      <div class="tagline">next generation skin care</div>
    </div>

    <div class="divider"></div>

    <div class="contact">
      <div class="contact__title"><span class="accent">VELORA</span> HUID</div>

      <p class="contact__address">Lindenhofkade 42B, 3017KP<br>Rotterdam</p>
      <p class="contact__line">
        <svg class="icon" viewBox="0 0 16 16" aria-hidden="true"><path d="M1 6c0-2 3-3.5 7-3.5S15 4 15 6v1.2h-3.2V5.6H4.2v1.6H1z"/><path d="M4 8h8l2 5.5H2z"/><circle cx="8" cy="10.5" r="1.6" fill="#fff"/></svg>
        010 438 21 95
      </p>

      <p class="contact__address">Zonnewijzerstraat 73, 1062HT<br>Amsterdam</p>
      <p class="contact__line">
        <svg class="icon" viewBox="0 0 16 16" aria-hidden="true"><path d="M1 6c0-2 3-3.5 7-3.5S15 4 15 6v1.2h-3.2V5.6H4.2v1.6H1z"/><path d="M4 8h8l2 5.5H2z"/><circle cx="8" cy="10.5" r="1.6" fill="#fff"/></svg>
        020 519 8372
      </p>

      <p class="contact__line contact__line--email">
        <svg class="icon" viewBox="0 0 16 16" aria-hidden="true"><path d="M1 3.5h14v9H1z"/><path d="M1.5 4l6.5 5 6.5-5" fill="none" stroke="#fff" stroke-width="1.2"/></svg>
        info@velorahuid.nu
      </p>
      <p class="contact__line contact__line--web">
        <svg class="icon" viewBox="0 0 16 16" aria-hidden="true"><circle cx="8" cy="8" r="7"/><path d="M1 8h14M8 1c-3 3.5-3 10.5 0 14M8 1c3 3.5 3 10.5 0 14" fill="none" stroke="#fff" stroke-width="1"/></svg>
        www.velorahuid.nu
      </p>
    </div>
  </section>

</div>
</body>
</html>
```